The B.O.L.D. Initiative Display Poster

We need a design for a Display Poster (33"W x 73"H) for an expo we are attending May 9th.

Our website is www.boldinitiative-example.org for more information

We are a 501(c)3 that works with youth who have been commercially sexual exploited. We have a California Licensed Therapeutic Residential Program, Drop-In Center and Thrift Store.

B.O.L.D. stands for Brave, Open, Lively and Determined

Our Full logo and Logo without Text is attached. Our mission is:
"Empowers youth to break away from Commercial Sexual Exploitation and Evolve from Victims to Leaders"

We want the design to highlight to phoenix logo, as well as indicate our mission statement.

The B.O.L.D. Initiative offers the following for youth who have been commercially sexually exploited:

• A California licensed (level 12) therapeutic residential program (GROWING at home)
• A drop-in center (open 3pm-7pm Mondays through Fridays) (GROWING forward)
• A Thrift Store where 100% of the proceeds benefit The B.O.L.D. Initiative (GROWING beyond)
The B.O.L.D. Initiative is:
• Survivor-Led
• Trauma Informed
• Strengths Based
• Culturally and Gender Responsive
• A model utilizing Harm Reduction coupled with Empowerment

Target Market(s)

Non-Profits, Possible Grant Organizations, Youth who have been commercially sexually exploited as children (CSEC)

Font styles to use
Serif

Colors
f68e4e
faa54b
fece3e
fbed22
9bcb3c
886aae
b768aa

Requirements
Must have
• Positive, empowering imagery.
Nice to have
• Inspiring imagery. want to inspire hope, strength, resilience
Should not have
• Negative, chains, imprisonment imagery

```html
<!DOCTYPE html>
<html lang="en">
<head>
<meta charset="utf-8">
<title>The B.O.L.D. Initiative – Display Poster Options</title>
<link href="https://fonts.googleapis.com/css2?family=Questrial&display=swap" rel="stylesheet">
<style>
  :root {
    --purple: #55276f;
    --purple-deep: #4a2164;
    --brand-purple: #5b2a82;
    --yellow: #f3e93a;
    --white: #ffffff;
    --black: #000000;
    --orange: #e98a2e;
    --ribbon-orange: #ef8b30;
    --red: #e8262e;
    --green: #9bcb3c;
    --grad-yellow: #f4d232;
    --grad-orange: #ee8a2c;
    --grad-red: #da2a2c;
    --grad-crimson: #c32146;
    --circle: #f68e4e;
  }
  * { margin: 0; padding: 0; box-sizing: border-box; }
  html, body { width: 1200px; height: 1000px; overflow: hidden; background: var(--white); }
  body { position: relative; font-family: "Questrial", "Century Gothic", sans-serif; }

  .option-label {
    position: absolute; top: 500px; font-size: 38px; color: var(--black);
    transform: translate(-50%, -50%) rotate(-90deg); white-space: nowrap;
  }
  .option-label--one { left: 44px; }
  .option-label--two { left: 1156px; }

  .poster { position: absolute; top: 0; height: 1000px; background: var(--black); overflow: hidden; }
  .poster--one { left: 86px; width: 470px; }
  .poster--two { left: 626px; width: 472px; }
  .poster__face { position: absolute; top: 0; bottom: 0; overflow: hidden; }
  .poster--one .poster__face { left: 17px; right: 0; background: var(--purple); }
  .poster--two .poster__face { left: 19px; right: 0;
    background: linear-gradient(180deg, var(--grad-yellow) 205px, var(--grad-orange) 400px, var(--grad-red) 600px, var(--grad-crimson) 780px, var(--purple-deep) 1000px); }

  .masthead { position: absolute; left: 0; top: 0; width: 100%; }
  .masthead svg { display: block; }
  .poster--two .masthead { height: 205px; background: var(--white); }

  .brand { position: absolute; display: flex; align-items: center; gap: 22px; }
  .poster--one .brand { left: 20px; top: 28px; }
  .poster--two .brand { left: 42px; top: 28px; }
  .brand__dot { width: 140px; height: 140px; border-radius: 50%; background: var(--circle); flex: none; }
  .brand__name { font-size: 36px; line-height: 1.1; color: var(--brand-purple); text-align: center; width: 200px; }

  .mission { position: absolute; left: 0; width: 100%; top: 262px; text-align: center; font-size: 29px; line-height: 37.8px; color: var(--yellow); }
  .mission .big { font-size: 32px; }
  .mission .hl { color: var(--white); }
  .poster--two .mission { color: var(--white); }
  .poster--two .mission .hl { color: var(--black); }

  .details { position: absolute; top: 538px; left: 26px; width: 420px; font-size: 13.2px; line-height: 16.6px; color: var(--orange); }
  .details h3 { font-weight: normal; font-size: 13.2px; color: var(--red); }
  .details ul { list-style: none; margin: 8px 0 17px; }
  .details li { padding-left: 13px; text-indent: -13px; }
  .details li::before { content: "•"; display: inline-block; width: 13px; text-indent: 0; }
  .poster--two .details { color: var(--white); }
  .poster--two .details h3 { color: var(--white); }

  .help-band { position: absolute; left: 0; right: 0; top: 883px; height: 37px; background: var(--green); }
  .help-ribbon { position: absolute; left: 0; top: 872px; }
  .help-ribbon__text { position: absolute; left: 72px; width: 308px; top: 885px; text-align: center; font-size: 25px; color: var(--white); }
  .contact-area { position: absolute; left: 0; right: 0; top: 930px; bottom: 0; background: var(--white); }
  .contact { position: absolute; left: 0; width: 100%; text-align: center; color: var(--black); }
  .contact__call { font-size: 20px; line-height: 24px; }
  .contact__call .number { color: var(--red); font-size: 23px; }
  .contact__hours { font-size: 18px; line-height: 22px; }
  .poster--one .contact { top: 940px; }

  .help-pill { position: absolute; left: 87px; top: 885px; width: 278px; height: 42px; background: var(--black);
    border-radius: 14px 14px 0 0; color: var(--white); font-size: 25px; text-align: center; line-height: 42px; }
  .contact-box { position: absolute; left: 27px; top: 925px; width: 398px; height: 64px; background: var(--white); border-radius: 14px; }
  .poster--two .contact { top: 932px; }
</style>
</head>
<body>
  <div class="option-label option-label--one">Option 1</div>
  <div class="option-label option-label--two">Option 2</div>

  <section class="poster poster--one">
    <div class="poster__face">
      <div class="masthead">
        <svg width="453" height="245" viewBox="0 0 453 245" aria-hidden="true">
          <path d="M0 0 H453 V140 Q453 158 436 162 L0 238 Z" fill="#ffffff"/>
        </svg>
      </div>
      <div class="brand">
        <div class="brand__dot"></div>
        <div class="brand__name">The B.O.L.D. Initiative</div>
      </div>

      <h1 class="mission" style="font-weight:normal">
        Empowers <span class="hl">youth</span> to<br>
        break away from<br>
        Commercial<br>
        <span class="hl big">Sexual Exploitation</span><br>
        and Evolve from<br>
        <span class="hl big">Victims</span> to Leaders
      </h1>

      <div class="details">
        <h3>The B.O.L.D. Initiative offers the following for youth who have been commercially sexually exploited:</h3>
        <ul>
          <li>A California licensed (level 12) therapeutic residential program (GROWING at home)</li>
          <li>A drop-in center (open 3pm-7pm Mondays through Fridays) (GROWING forward)</li>
          <li>A Thrift Store where 100% of the proceeds benefit The B.O.L.D. Initiative (GROWING beyond)</li>
        </ul>
        <h3>The B.O.L.D. Initiative is:</h3>
        <ul>
          <li>Survivor-Led</li>
          <li>Trauma Informed</li>
          <li>Strengths Based</li>
          <li>Culturally and Gender Responsive</li>
          <li>A model utilizing Harm Reduction coupled with Empowerment</li>
        </ul>
      </div>

      <div class="help-band"></div>
      <svg class="help-ribbon" width="453" height="60" viewBox="0 0 453 60" aria-hidden="true">
        <polygon points="52,11 72,1 72,59 52,48" fill="#c46a1e"/>
        <polygon points="400,11 380,1 380,59 400,48" fill="#c46a1e"/>
        <rect x="72" y="1" width="308" height="58" fill="#ef8b30"/>
      </svg>
      <div class="help-ribbon__text">For Immediate Help</div>

      <div class="contact-area"></div>
      <div class="contact">
        <div class="contact__call">CALL: <span class="number">855-4-BE BOLD</span></div>
        <div class="contact__hours">24 Hours a Day / 7 Days a Week</div>
      </div>
    </div>
  </section>

  <section class="poster poster--two">
    <div class="poster__face">
      <div class="masthead"></div>
      <div class="brand">
        <div class="brand__dot"></div>
        <div class="brand__name">The B.O.L.D. Initiative</div>
      </div>

      <h1 class="mission" style="font-weight:normal">
        Empowers <span class="hl">youth</span> to<br>
        break away from<br>
        Commercial<br>
        <span class="hl big">Sexual Exploitation</span><br>
        and Evolve from<br>
        <span class="hl big">Victims</span> to Leaders
      </h1>

      <div class="details">
        <h3>The B.O.L.D. Initiative offers the following for youth who have been commercially sexually exploited:</h3>
        <ul>
          <li>A California licensed (level 12) therapeutic residential program (GROWING at home)</li>
          <li>A drop-in center (open 3pm-7pm Mondays through Fridays) (GROWING forward)</li>
          <li>A Thrift Store where 100% of the proceeds benefit The B.O.L.D. Initiative (GROWING beyond)</li>
        </ul>
        <h3>The B.O.L.D. Initiative is:</h3>
        <ul>
          <li>Survivor-Led</li>
          <li>Trauma Informed</li>
          <li>Strengths Based</li>
          <li>Culturally and Gender Responsive</li>
          <li>A model utilizing Harm Reduction coupled with Empowerment</li>
        </ul>
      </div>

      <div class="help-pill">For Immediate Help</div>
      <div class="contact-box"></div>
      <div class="contact">
        <div class="contact__call">CALL: <span class="number">855-4-BE BOLD</span></div>
        <div class="contact__hours">24 Hours a Day / 7 Days a Week</div>
      </div>
    </div>
  </section>
</body>
</html>
```